Velvet Lantern Poster

Marlowe Hall Ballet Academy presents
The Velvet Lantern
Friday December 19, 2014 7:30 PM
Brannock Playhouse at the Halvern State College

```html
<!DOCTYPE html>
<html lang="en">
<head>
<meta charset="utf-8">
<title>The Velvet Lantern Poster</title>
<link href="https://fonts.googleapis.com/css2?family=Great+Vibes&family=Poppins:wght@600;700&display=swap" rel="stylesheet">
<style>
  :root {
    --page-bg: #2b3140;
    --frame: #ffffff;
    --pink: #f06fb4;
    --pink-deep: #e0559f;
    --ink: #111111;
    --sky-top: #3a4f6e;
    --sky-mid: #6f7f97;
    --sunset: #e59a45;
    --sea: #3c4e63;
    --dune: #2a2e2c;
    --boardwalk: #6c7a8a;
  }
  * { margin: 0; padding: 0; box-sizing: border-box; }
  html, body { width: 1200px; height: 1000px; overflow: hidden; }
  body {
    background: var(--page-bg);
    font-family: "Poppins", Arial, sans-serif;
    position: relative;
  }
  .poster {
    position: absolute;
    left: 205px;
    top: 0;
    width: 790px;
    height: 1000px;
    background: var(--frame);
    padding: 0 12px;
  }
  .poster-scene {
    position: absolute;
    inset: 0 12px;
    background: linear-gradient(
      to bottom,
      var(--sky-top) 0%,
      var(--sky-mid) 18%,
      #8a7f7a 30%,
      var(--sunset) 38%,
      #b8773f 42%,
      var(--sea) 46%,
      #34414f 52%,
      var(--dune) 60%,
      var(--boardwalk) 78%,
      #4a5563 100%
    );
  }
  .outlined {
    color: var(--pink);
    -webkit-text-stroke: 5px #ffffff;
    paint-order: stroke fill;
    text-shadow: 0 2px 4px rgba(0,0,0,.55);
    text-align: center;
    position: absolute;
    left: 12px;
    right: 12px;
  }
  .presenter {
    top: 30px;
    font-weight: 700;
    font-size: 22px;
    -webkit-text-stroke-width: 4px;
  }
  .title { position: absolute; left: 12px; right: 12px; top: 470px; height: 170px; }
  .title-article {
    font-family: "Great Vibes", cursive;
    font-size: 64px;
    left: auto;
    right: 140px;
    top: 0;
    text-align: left;
  }
  .title-main {
    font-family: "Great Vibes", cursive;
    font-size: 112px;
    line-height: 1;
    top: 52px;
    -webkit-text-stroke-width: 7px;
  }
  .date { top: 660px; font-weight: 700; font-size: 36px; line-height: 1.2; }
  .time { top: 710px; font-weight: 700; font-size: 36px; line-height: 1.2; }
  .venue { top: 768px; font-weight: 700; font-size: 22px; line-height: 1.2; }
  .brand-box {
    position: absolute;
    left: 70px;
    top: 905px;
    width: 168px;
    height: 92px;
    background: var(--frame);
    display: flex;
    align-items: center;
    justify-content: center;
    gap: 10px;
  }
  .brand-dot {
    width: 18px; height: 18px;
    border-radius: 50%;
    background: var(--pink-deep);
  }
  .brand-name {
    font-weight: 700;
    font-size: 30px;
    color: var(--ink);
  }
  .tickets {
    position: absolute;
    left: 257px;
    top: 885px;
    width: 503px;
    height: 90px;
    background: var(--frame);
    color: var(--ink);
    text-align: center;
    font-weight: 600;
    font-size: 21px;
    line-height: 1.3;
    padding-top: 14px;
  }
</style>
</head>
<body>
  <main class="poster">
    <div class="poster-scene" role="img" aria-label="Photo of a ballerina silhouette in a tutu on a beach boardwalk at sunset, with pink butterflies trailing from her hand"></div>

    <p class="outlined presenter">Marlowe Hall Ballet Academy presents...</p>

    <h1 class="title">
      <span class="outlined title-article">The</span>
      <span class="outlined title-main">Velvet Lantern</span>
    </h1>

    <p class="outlined date">Friday December 19, 2014</p>
    <p class="outlined time">7:30 PM</p>
    <p class="outlined venue">Brannock Playhouse at the Halvern State College</p>

    <div class="brand-box">
      <span class="brand-dot"></span>
      <span class="brand-name">MHB</span>
    </div>

    <div class="tickets">
      for tickets visit:<br>
      www.marlowehallballet.org
    </div>
  </main>
</body>
</html>
```